I have a basic design of a poster that I want to make look better. The poster is a list of continuing medical education rules.

JRPPS = Joint Registry for Postgraduate Physician Studies This text should be included. You might also want to include "CME". Please use all the existing elements in the file.

I want to sell this poster to CME offices around the US. The poster should be 24 by 36

Reason: I would like to see more designs. I have received less than ten.

Target Market(s)

CME professionals

Industry/Entity Type

Medical

Colors

Designer to choose colors to be used in the design.

Requirements
Must have
• All elements in the file provided. You can also spell out Joint Registry for Postgraduate Physician Studies.

```html
<!DOCTYPE html>
<html lang="en">
<head>
<meta charset="utf-8">
<title>JRPPS Accreditation Criteria Poster</title>
<link href="https://fonts.googleapis.com/css2?family=Arimo:wght@400;700&family=Archivo:wght@800&family=Open+Sans:wght@400;600&family=Roboto+Condensed:wght@300&display=swap" rel="stylesheet">
<style>
:root{
  --backdrop:#5f5f5f;
  --paper:#ffffff;
  --band-dark:#1b3f8f;
  --band-mid:#2a6fd0;
  --band-light:#4fa3e8;
  --panel:#d9d9d9;
  --ink:#1a1a1a;
  --bar-light:#9fb4c6;
  --bar-mid:#73879a;
  --bar-dark:#515c66;
  --bar-grey:#a8a8a8;
}
*{margin:0;padding:0;box-sizing:border-box}
html,body{width:1200px;height:1000px;overflow:hidden;background:var(--backdrop)}
.poster{position:absolute;left:298px;top:40px;width:615px;height:923px;background:var(--paper);box-shadow:0 0 12px rgba(0,0,0,.35);font-family:Arimo,Arial,sans-serif}
.masthead{position:absolute;left:15px;top:15px;width:584px;height:68px;border-radius:6px;background:linear-gradient(180deg,var(--band-light),var(--band-mid) 45%,var(--band-dark));color:#fff}
.brand{position:absolute;left:0;top:6px;width:240px;text-align:center}
.brand-name{font-family:"Open Sans",sans-serif;font-weight:400;font-size:30px;letter-spacing:6px;line-height:34px}
.brand-full{font-family:"Open Sans",sans-serif;font-size:8.5px;line-height:11px;letter-spacing:.3px;text-transform:uppercase;width:180px;margin:0 auto}
.intro{position:absolute;left:245px;top:7px;width:335px;font-family:"Open Sans",sans-serif;font-size:7.6px;line-height:10.5px}
.section-title{position:absolute;left:0;width:100%;text-align:center;font-family:Archivo,sans-serif;font-weight:800;font-size:17px;letter-spacing:.5px;color:var(--ink)}
.criteria-panel{position:absolute;left:15px;top:115px;width:584px;height:618px;border-radius:10px;background:linear-gradient(90deg,#cfcfcf,#e6e6e6 60%,#d6d6d6)}
.panel-label{position:absolute;left:67px;top:425px;transform:translate(-50%,-50%) rotate(-90deg);font-family:"Roboto Condensed",sans-serif;font-weight:300;font-size:52px;letter-spacing:2px;color:#f3f3f3;text-shadow:0 0 2px #aaa}
.criterion{position:absolute;height:40px;left:0;width:615px}
.badge{position:absolute;top:-2px;width:44px;height:44px;border-radius:50%;background:radial-gradient(circle at 40% 35%,#fff,#d6d6d6);box-shadow:0 1px 3px rgba(0,0,0,.35)}
.badge span{position:absolute;left:7px;top:7px;width:30px;height:30px;border-radius:50%;color:#fff;font-size:15px;line-height:30px;text-align:center;font-family:"Roboto Condensed",sans-serif;font-weight:300}
.connector{position:absolute;top:19px;height:2px;background:linear-gradient(90deg,#fff,rgba(255,255,255,.2))}
.statement{position:absolute;top:2px;width:345px;height:36px;border-radius:2px;border:1px solid #f2f2f2;box-shadow:1px 1px 2px rgba(0,0,0,.3);color:#fff;font-size:7.6px;line-height:9.2px;padding:0 10px 0 20px;display:flex;align-items:center}
.odd .badge{left:95px}.odd .connector{left:137px;width:50px}.odd .statement{left:185px}
.even .badge{left:128px}.even .connector{left:170px;width:50px}.even .statement{left:217px}
.light{background:var(--bar-light)}.mid{background:var(--bar-mid)}.dark{background:var(--bar-dark)}.retired{background:var(--bar-grey)}
.commendation{position:absolute;left:15px;top:760px;width:584px;height:110px;display:flex}
.commendation-item{flex:1;padding:4px 5px;font-size:7.6px;line-height:8.6px;color:var(--ink)}
.commendation-item h3{font-family:Arimo,sans-serif;font-weight:700;font-size:11.5px;line-height:14px;margin-bottom:1px}
.footer-band{position:absolute;left:15px;top:876px;width:584px;height:24px;background:linear-gradient(180deg,var(--band-light),var(--band-mid) 45%,var(--band-dark));color:#fff;text-align:center;font-weight:700;font-size:12px;line-height:24px}
</style>
</head>
<body>
<main class="poster">
  <header class="masthead">
    <div class="brand">
      <div class="brand-name">JRPPS</div>
      <div class="brand-full">Joint Registry for Postgraduate Physician Studies</div>
    </div>
    <p class="intro">The Accreditation Criteria are divided into three levels. To achieve Provisional Accreditation, a two year term, providers must comply with Criteria 1, 2, 3, and 7-12. Providers seeking full Accreditation or reaccredition for a four - year term must comply with Criteria 1-13. To achieve Accreditation with Commendation, a six - year term, providers must comply with all Accreditation Criteria</p>
  </header>

  <h1 class="section-title" style="top:91px">ACCREDITATION CRITERIA</h1>

  <section class="criteria-panel"></section>
  <div class="panel-label">CRITERION</div>

  <div class="criterion odd" style="top:120px"><div class="badge"><span style="background:#e8590c">01</span></div><div class="connector"></div><div class="statement light">The provider has a CME mission statement that includes expected results articulated in terms of changes in competence, performance, or patient outcomes that will be the result of the program.</div></div>
  <div class="criterion even" style="top:160px"><div class="badge"><span style="background:#7a2150">02</span></div><div class="connector"></div><div class="statement mid">The provider incorporates into CME activities the education needs (knowledge, competence, or performance) that underlie the professional practice gaps of their own learners.</div></div>
  <div class="criterion odd" style="top:201px"><div class="badge"><span style="background:#3aa935">03</span></div><div class="connector"></div><div class="statement dark">The provider generates activities / educational interventions that are designed to change competence, performance, or patient outcomes as described in its mission statement.</div></div>
  <div class="criterion even" style="top:241px"><div class="badge"><span style="background:#9c9c9c">04</span></div><div class="connector"></div><div class="statement retired">This criterion has been eliminated effective February 2014.</div></div>
  <div class="criterion odd" style="top:281px"><div class="badge"><span style="background:#e8482e">05</span></div><div class="connector"></div><div class="statement light">The provider chooses educational formats for activities / interventions that are appropriate for the setting, objectives, and desired results of the activity.</div></div>
  <div class="criterion even" style="top:322px"><div class="badge"><span style="background:#2aa5b3">06</span></div><div class="connector"></div><div class="statement mid">The provider develops activities educational interjections in the context of desirable physician attributes [e.g. National Health Sciences Institute (NHSI) competencies, Graduate Training Council (GTC) Competencies].</div></div>
  <div class="criterion odd" style="top:362px"><div class="badge"><span style="background:#e0357f">07</span></div><div class="connector"></div><div class="statement dark">The provider develops activities / education interventions independent of commercial interests. (SCS 1, 2 and 6).</div></div>
  <div class="criterion even" style="top:403px"><div class="badge"><span style="background:#5660a8">08</span></div><div class="connector"></div><div class="statement light">The provider appropriately manages commercial support (if applicable, SCS 3 of the JRPPS Standards for Commercial Support SM).</div></div>
  <div class="criterion odd" style="top:443px"><div class="badge"><span style="background:#a34a2c">09</span></div><div class="connector"></div><div class="statement mid">The provider maintains a separation of promotion from education (SCS 4).</div></div>
  <div class="criterion even" style="top:484px"><div class="badge"><span style="background:#2e9a2e">10</span></div><div class="connector"></div><div class="statement dark">The provider actively promotes improvements in health care and NOT proprietary interests of a commercial interest (SCS5).</div></div>
  <div class="criterion odd" style="top:524px"><div class="badge"><span style="background:#767263">11</span></div><div class="connector"></div><div class="statement light">The provider analyzes changes in earners (competence, performance, or patient outcomes) achieved as a result of the overall program's activities / educational interventions.</div></div>
  <div class="criterion even" style="top:565px"><div class="badge"><span style="background:#e24a1c">12</span></div><div class="connector"></div><div class="statement mid">The provider gathers data or information and conducts a program - based analysis on the degree to which the CME mission of the provider has been met through the conduct of CME activities / educational interventions.</div></div>
  <div class="criterion odd" style="top:606px"><div class="badge"><span style="background:#1f5aa6">13</span></div><div class="connector"></div><div class="statement dark">The provider identifies, plans and implements the overall program (e.g. planners, teachers, infrastructure, methods, resources, facilities, interventions) that are required to improve on ability to meet the CME mission.</div></div>
  <div class="criterion even" style="top:647px"><div class="badge"><span style="background:#7c9474">14</span></div><div class="connector"></div><div class="statement retired">This criterion has been eliminated effective February 2014.</div></div>
  <div class="criterion odd" style="top:687px"><div class="badge"><span style="background:#f2a81d">15</span></div><div class="connector"></div><div class="statement retired">This criterion has been eliminated effective February 2014.</div></div>

  <h2 class="section-title" style="top:739px">ACCREDITATION WITH COMMENDATION</h2>

  <section class="commendation">
    <div class="commendation-item" style="background:#a8dcc0"><h3>Criterion 16</h3>The provider operates in a manner that integrates CME into the process for improving professional practice.</div>
    <div class="commendation-item" style="background:#f6bcaa"><h3>Criterion 17</h3>The provider utilizes non-education strategies to enhance change as an adjunct to its activities / educationa interventions (eg. reminders, patient feedback).</div>
    <div class="commendation-item" style="background:#b3a9d6"><h3>Criterion 18</h3>The provider identifies factors outside the provider's control that impact on patient outcomes.</div>
    <div class="commendation-item" style="background:#6cc3ee"><h3>Criterion 19</h3>The provider implements educational strategies to remove, overcome or address barriers to phsician change.</div>
    <div class="commendation-item" style="background:#bfb655"><h3>Criterion 20</h3>The provider builds bridges with other stake holders through collaboration and cooperation.</div>
    <div class="commendation-item" style="background:#f8c08c"><h3>Criterion 21</h3>The provider participates within an institutional or system framework for quality improvement.</div>
    <div class="commendation-item" style="background:#b9dd74"><h3>Criterion 22</h3>The provider is positioned to influence the scope and content of activities / educational interventions.</div>
  </section>

  <footer class="footer-band">www.jrpps.org</footer>
</main>
</body>
</html>
```